Invitation Design Project

I would like to have a custom invitation (and reception/response cards) designed for my son's Bar Mitzvah. I have a strong idea of what I want and have a few mock-ups, but my "home made" effort would be improved by the addition of professional creativity and skill. The invitation should be white, red, and black, and a bold typographic style (see attachment). I am looking for a clean modern feel, and prefer square shaped invitations. I need the final product in an electronic format that I could either print myself or have done at a local printer.

Target Market(s)

Guests to a Bar Mitzvah. A group of family and friends ranging from 40-60 years of age, and a group of my son's 13 year old friends.

Industry/Entity Type

Electronic

Requirements
Must have
• Square shaped invitation (exact dimensions in attached file)
Typographic style
Red, black, white
Red color should be CMYK: 30-96-76-26
Nice to have
• I like the two icons on my attached sample reception card, especially the swirl/Torah one. I would be nice to use these (or similar ones) if there is a way to do so, but this is not a requirement.

```html
<!DOCTYPE html>
<html lang="en">
<head>
<meta charset="utf-8">
<title>Invitation Design</title>
<link rel="stylesheet" href="https://fonts.googleapis.com/css2?family=Marcellus&family=Montserrat:wght@500;600;700&family=Questrial&display=swap">
<style>
  :root{
    --red:#8c2033;
    --ink:#111111;
    --paper:#ffffff;
    --label:#7a7a7a;
    --title:#6a6a6a;
    --bg-center:#ffffff;
    --bg-edge:#c4c4c4;
  }
  html,body{margin:0;padding:0;overflow:hidden;}
  .canvas{
    position:relative;width:1200px;height:1000px;overflow:hidden;
    background:radial-gradient(ellipse 620px 520px at 600px 470px,var(--bg-center) 0%,#ececec 55%,var(--bg-edge) 100%);
    font-family:"Questrial",sans-serif;color:var(--ink);
  }
  .abs{position:absolute;}
  .page-title{
    position:absolute;left:0;top:72px;width:1200px;text-align:center;margin:0;font-weight:400;
    font-family:"Marcellus",serif;font-size:76px;color:var(--title);
    text-shadow:2px 3px 3px rgba(0,0,0,.25);letter-spacing:1px;
  }
  .piece-label{
    position:absolute;font-family:"Marcellus",serif;font-size:26px;color:var(--label);
    text-shadow:1px 2px 2px rgba(0,0,0,.18);white-space:nowrap;
  }
  .card{position:absolute;background:var(--paper);box-shadow:2px 3px 6px rgba(0,0,0,.35);overflow:hidden;}
  .frame{position:absolute;border-style:solid;border-color:var(--red);box-sizing:border-box;}
  .tab{position:absolute;background:var(--red);}
  .flourish{position:absolute;width:42px;height:10px;background:var(--red);border-radius:5px;opacity:.85;}
  .line{position:absolute;text-align:center;white-space:nowrap;text-transform:uppercase;}
  .rule{position:absolute;background:var(--red);}

  /* invitation */
  .invite-intro{font-size:12.5px;letter-spacing:.6px;}
  .invite-name{font-family:"Montserrat",sans-serif;font-weight:600;font-size:63px;color:var(--red);letter-spacing:9px;line-height:1;}
  .invite-sub{font-size:12.5px;letter-spacing:1.4px;}
  .date-col{position:absolute;font-size:14.5px;letter-spacing:.9px;line-height:20px;text-transform:uppercase;white-space:nowrap;}
  .venue{font-size:12px;letter-spacing:.4px;}
  .venue-note{font-size:7.6px;letter-spacing:0;}

  /* reception */
  .reception-band{position:absolute;left:0;top:0;width:98px;height:310px;background:var(--red);}
  .band-rule{position:absolute;left:10px;width:81px;height:1.5px;background:var(--paper);}
  .band-text{position:absolute;left:0;width:98px;text-align:center;color:var(--paper);font-size:11.5px;letter-spacing:.5px;line-height:13px;}
  .reception-heading{position:absolute;left:110px;top:29px;font-family:"Montserrat",sans-serif;font-weight:600;font-size:24px;color:var(--red);letter-spacing:0;white-space:nowrap;}
  .dash{position:absolute;left:111px;width:156px;border-top:1px dashed #555;}
  .reception-text{position:absolute;left:111px;font-size:11.5px;letter-spacing:.4px;line-height:18.5px;white-space:nowrap;}

  /* response */
  .response-heading{font-family:"Montserrat",sans-serif;font-weight:600;font-size:16.5px;color:var(--red);line-height:19px;}
  .response-text{font-size:8.8px;letter-spacing:.2px;line-height:15px;}
  .check{position:absolute;width:26px;height:26px;border:2px solid var(--red);}
  .check-label{position:absolute;font-size:8.5px;width:60px;text-align:center;}
</style>
</head>
<body>
<div class="canvas">
  <h1 class="page-title">Invitation Design</h1>

  <div class="piece-label" style="left:158px;top:400px;">Invitation</div>
  <div class="piece-label" style="left:958px;top:395px;">Reception Card</div>
  <div class="piece-label" style="left:69px;top:765px;">Respondive Card</div>
  <div class="piece-label" style="left:960px;top:770px;">TDB Card</div>

  <!-- Invitation -->
  <section class="card invitation" style="left:292px;top:260px;width:338px;height:338px;">
    <div class="frame" style="left:12px;top:11px;width:314px;height:315px;border-width:9px;"></div>
    <div class="tab" style="left:0;top:135px;width:14px;height:86px;"></div>
    <div class="tab" style="right:0;top:135px;width:14px;height:86px;"></div>
    <div class="flourish" role="img" aria-label="decorative flourish" style="left:148px;top:28px;"></div>

    <div class="line invite-intro" style="left:0;width:338px;top:49px;">It is with great pride and joy that</div>
    <div class="line invite-intro" style="left:0;width:338px;top:67px;">we invite you to join us as our son</div>
    <div class="line invite-name" style="left:0;width:338px;top:78px;padding-left:9px;box-sizing:border-box;">Ethan</div>
    <div class="line invite-sub" style="left:0;width:338px;top:139px;">Celebrate his Bar Mitzvah</div>
    <div class="rule" style="left:35px;top:157px;width:271px;height:2px;"></div>

    <div class="date-col" style="left:32px;top:163px;">Saturday<br>September<br>Twenty Eight</div>
    <div class="rule" style="left:168px;top:165px;width:2px;height:55px;"></div>
    <div class="date-col" style="left:179px;top:163px;">Two<br>Thousand<br>And Thirteen</div>
    <div class="rule" style="left:35px;top:223px;width:271px;height:2px;"></div>

    <div class="line venue" style="left:0;width:338px;top:231px;">Riverside Hebrew Congregation</div>
    <div class="line venue" style="left:0;width:338px;top:248px;">2217 Linden Avenue Ashford, Virginia</div>
    <div class="line venue-note" style="left:0;width:338px;top:266px;">Please join us for a kiddush immediately following the service</div>
    <div class="line venue" style="left:0;width:338px;top:280px;">Rachel Stein</div>
    <div class="flourish" role="img" aria-label="decorative flourish" style="left:148px;top:303px;"></div>
  </section>

  <!-- Reception card -->
  <section class="card reception" style="left:657px;top:287px;width:278px;height:310px;">
    <div class="reception-band">
      <div class="band-rule" style="top:12px;"></div>
      <svg class="abs" style="left:20px;top:48px;" width="58" height="58" viewBox="0 0 58 58" aria-hidden="true">
        <path d="M30 2 C22 7 36 10 28 17" fill="none" stroke="#fff" stroke-width="3" stroke-linecap="round"/>
        <circle cx="29" cy="27" r="2.6" fill="#fff"/>
        <path d="M8 48 A21 20 0 0 1 50 48 Z" fill="#fff"/>
        <rect x="3" y="50" width="52" height="3" rx="1.5" fill="#fff"/>
      </svg>
      <div class="band-text" style="top:110px;">10:30 A.M.<br>SERVICE</div>
      <svg class="abs" style="left:13px;top:180px;" width="72" height="50" viewBox="0 0 72 50" aria-hidden="true">
        <circle cx="36" cy="25" r="18" fill="none" stroke="#fff" stroke-width="2.5"/>
        <circle cx="36" cy="25" r="12" fill="none" stroke="#fff" stroke-width="2"/>
        <path d="M3 4 V14 M6 4 V14 M9 4 V14 M3 14 Q6 19 9 14" fill="none" stroke="#fff" stroke-width="1.6"/>
        <rect x="4.8" y="16" width="2.6" height="31" rx="1.3" fill="#fff"/>
        <path d="M66 3 Q70 14 68 26 L66 26 Z" fill="#fff"/>
        <rect x="64.7" y="24" width="2.6" height="23" rx="1.3" fill="#fff"/>
      </svg>
      <div class="band-text" style="top:234px;">1:00 P.M.<br>RECEPTION</div>
      <div class="band-rule" style="top:294px;"></div>
    </div>
    <div class="flourish" role="img" aria-label="decorative flourish" style="left:168px;top:9px;"></div>
    <div class="reception-heading">RECEPTION</div>
    <div class="dash" style="top:69px;"></div>
    <div class="dash" style="top:81px;"></div>
    <div class="dash" style="top:93px;"></div>
    <div class="dash" style="top:106px;"></div>
    <div class="dash" style="top:118px;"></div>
    <div class="dash" style="top:131px;"></div>
    <div class="reception-text" style="top:143px;">1:00 - 4:30 P.M.</div>
    <div class="rule" style="left:111px;top:182px;width:156px;height:2px;"></div>
    <div class="reception-text" style="top:214px;">THE MAPLE HALL<br>3580 ORCHARD HILL RD<br>FAIRVIEW, VA 22999</div>
    <div class="flourish" role="img" aria-label="decorative flourish" style="left:168px;top:289px;"></div>
  </section>

  <!-- Response card -->
  <section class="card response" style="left:325px;top:631px;width:216px;height:309px;">
    <div class="frame" style="left:9px;top:9px;width:198px;height:292px;border-width:7px;"></div>
    <div class="tab" style="left:0;top:94px;width:10px;height:120px;"></div>
    <div class="tab" style="right:0;top:94px;width:10px;height:120px;"></div>
    <div class="flourish" role="img" aria-label="decorative flourish" style="left:87px;top:27px;width:34px;"></div>
    <div class="line response-heading" style="left:0;width:216px;top:53px;">Responsive<br>Card</div>
    <div class="line response-text" style="left:0;width:216px;top:108px;">The favor of a reply is requested<br>by the twenty first of August<br>two thousand thirteen</div>
    <div class="check" style="left:61px;top:174px;"></div>
    <div class="check" style="left:122px;top:174px;"></div>
    <div class="check-label" style="left:46px;top:205px;">ACCEPT</div>
    <div class="check-label" style="left:107px;top:205px;">REGRETS</div>
    <div class="check-label" style="left:26px;top:237px;width:40px;text-align:left;">NAMES:</div>
    <div class="rule" style="left:59px;top:246px;width:127px;height:1px;"></div>
    <div class="rule" style="left:59px;top:256px;width:127px;height:1px;"></div>
    <div class="flourish" role="img" aria-label="decorative flourish" style="left:84px;top:272px;width:34px;"></div>
  </section>

  <!-- TDB card -->
  <section class="card tdb" style="left:571px;top:631px;width:342px;height:309px;">
    <div class="frame" style="left:15px;top:14px;width:312px;height:281px;border-width:9px;"></div>
    <div class="tab" style="left:0;top:111px;width:16px;height:86px;"></div>
    <div class="tab" style="right:0;top:111px;width:16px;height:86px;"></div>
  </section>
</div>
</body>
</html>
```